Fun Location App for users to earn rewards and vouchers everywhere they go

Jorvix is a social app where users can collect rewards when they travel + complete quests at different location to get rewards.

We would like a design of an app that has these features/function
1) Login/Signup Page
2) HomePage - A Map with your current location
- Show the location/stores aroudn
- Have a bag tab to press and get rewards
3) Quests Tab = show all the available tasks
4) Exchange Tab = all the items available for exchange vouchers and can click to know more
5) Wallet Tab = user profile + vouchers in their wallet
6) Partners Tab = Showcase all the partners and can click to know more
7) Claim functions

We have attached a visual example. Do feel free to change what is best fit too. We do need to exact measurements as well to create the app

Target Market(s)

Fun, people who like rewards and interact with friends

Font styles to use
Sans Serif

Colors
f78f20
fbed22
fbee3e

Requirements
Must have
• Yellow, fun interactive feeling.
Nice to have
• Pop up when click on things
Should not have
• nil

```html
<!DOCTYPE html>
<html lang="en">
<head>
<meta charset="utf-8">
<title>Jorvix – app screens</title>
<link href="https://fonts.googleapis.com/css2?family=Poppins:wght@300;400;500;600;700&display=swap" rel="stylesheet">
<style>
:root{
  --bg:#f2f2f2;
  --card:#ffffff;
  --ink:#3a3b4a;
  --muted:#9a9aa6;
  --faint:#c4c4cc;
  --line:#ececf0;
  --navy:#2f3044;
  --map:#3c3f5c;
  --black:#151515;
  --orange:#f78f20;
  --yellow:#fbed22;
  --yellow2:#fbee3e;
  --amber:#fbc30f;
  --title:#f9a51a;
}
*{box-sizing:border-box;margin:0;padding:0}
html,body{width:754px;height:1200px;overflow:hidden}
body{background:var(--bg);font-family:'Poppins',sans-serif;color:var(--ink);position:relative}
.phone{position:absolute;width:151px;height:324px;background:var(--card);border-radius:22px;box-shadow:0 2px 8px rgba(0,0,0,.05);overflow:hidden}
.phone>*{position:absolute}
.time{left:17px;top:17px;font-size:5px;font-weight:600}
.status{right:16px;top:17px;width:16px;height:5px}
.dark .time{color:#fff}
.screen-black{left:6px;top:10px;width:139px;height:307px;background:var(--black);border-radius:16px}
.notch{left:36px;top:10px;width:79px;height:14px;background:var(--card);border-radius:0 0 8px 8px}
.brand{display:flex;align-items:center;gap:2px;font-weight:600;font-size:9px;color:var(--ink);line-height:1}
.brand i{display:block;width:7px;height:7px;border-radius:50%;background:var(--amber)}
.menu{width:7px;height:5px;border-top:1px solid var(--ink);border-bottom:1px solid var(--ink)}
.menu::after{content:"";display:block;margin-top:1px;height:1px;background:var(--ink)}
.title{font-size:8.5px;font-weight:600;color:var(--title);line-height:1}
.sub{font-size:4px;color:var(--muted);line-height:1}
.row{left:6px;width:139px;height:29px;border-bottom:.5px solid var(--line)}
.row>*{position:absolute}
.thumb{left:11px;top:4px;width:23px;height:16px;border-radius:1px}
.t-night{background:linear-gradient(160deg,#2d6e9a,#0d2a44)}
.t-cafe{background:linear-gradient(90deg,#1b1b1b 55%,#a07850)}
.t-salon{background:linear-gradient(120deg,#e8e8ea,#bfc3c9)}
.rtext{left:36px;top:4px;width:60px;line-height:1.15}
.rtext b{display:block;font-weight:400;font-size:4px;color:var(--ink)}
.rtext span{display:block;font-size:2.6px;color:var(--muted)}
.pill{height:8px;border-radius:4px;background:linear-gradient(90deg,var(--yellow),var(--amber));color:#fff;font-size:3px;font-weight:600;display:flex;align-items:center;justify-content:center}
.row .pill{left:105px;top:8px;width:28px}
.nav{left:6px;bottom:6px;width:139px;height:22px;background:var(--navy);border-radius:0 0 16px 16px}
.nav-pin{left:61px;bottom:16px;width:28px;height:28px;border-radius:50%;background:var(--navy);border:2px solid var(--amber);box-shadow:0 0 0 2px #fff;display:flex;align-items:center;justify-content:center}
.nav-pin svg{width:13px;height:16px}
.field{left:10px;width:131px;height:16px;border-radius:8px;background:#fff;box-shadow:0 1px 3px rgba(0,0,0,.08);font-size:5px;color:var(--faint);padding-left:10px;display:flex;align-items:center}
.label{font-size:4px;color:var(--faint);left:22px}
.value{font-size:8.5px;font-weight:500;color:#a6a6ae;left:22px}
.menu-item{left:102px;font-size:4.2px;font-weight:600;color:#fff}
.pin-m{width:10px;height:13px}
</style>
</head>
<body>

<svg width="0" height="0" style="position:absolute">
  <defs>
    <symbol id="pin" viewBox="0 0 24 30"><path d="M12 1C6 1 1.5 5.6 1.5 11.2 1.5 19 12 29 12 29s10.5-10 10.5-17.8C22.5 5.6 18 1 12 1z" fill="#fbc30f"/><circle cx="12" cy="11.5" r="4.6" fill="#2f3044"/></symbol>
    <symbol id="pin-light" viewBox="0 0 24 30"><path d="M12 1C6 1 1.5 5.6 1.5 11.2 1.5 19 12 29 12 29s10.5-10 10.5-17.8C22.5 5.6 18 1 12 1z" fill="#fbc30f"/><circle cx="12" cy="11.5" r="4.6" fill="#3c3f5c"/></symbol>
    <symbol id="status" viewBox="0 0 32 10"><rect x="0" y="6" width="2" height="3" fill="currentColor"/><rect x="3" y="4.5" width="2" height="4.5" fill="currentColor"/><rect x="6" y="3" width="2" height="6" fill="currentColor"/><rect x="9" y="1.5" width="2" height="7.5" fill="currentColor"/><path d="M13.5 4.5a5 5 0 0 1 7 0M15 6.2a2.8 2.8 0 0 1 4 0" stroke="currentColor" stroke-width="1.2" fill="none"/><circle cx="17" cy="8" r="1" fill="currentColor"/><rect x="23" y="2" width="8" height="6" rx="1.2" fill="currentColor"/></symbol>
  </defs>
</svg>

<!-- Splash -->
<section class="phone dark" style="left:64px;top:170px">
  <div class="screen-black"></div>
  <div class="notch"></div>
  <span class="time" style="left:18px;top:19px">9:41</span>
  <svg class="status" style="top:19px;color:#fff"><use href="#status"/></svg>
  <div class="brand" style="left:44px;top:138px;flex-direction:column;gap:6px;font-size:17px;color:#fff;font-weight:600"><i style="width:16px;height:16px"></i>jorvix</div>
</section>

<!-- Onboarding -->
<section class="phone dark" style="left:64px;top:512px">
  <div class="screen-black"></div>
  <div class="notch"></div>
  <span class="time" style="left:14px;top:19px">9:41</span>
  <svg class="status" style="top:19px;right:18px;color:#fff"><use href="#status"/></svg>
  <div style="left:59px;top:134px;width:34px;height:34px;border-radius:50%;background:var(--amber)"></div>
  <div style="left:36px;top:184px;width:79px;height:2px;background:#fff;border-radius:1px"></div>
  <div style="left:36px;top:184px;width:59px;height:2px;background:linear-gradient(90deg,var(--yellow),var(--orange));border-radius:1px"></div>
  <div style="left:0;width:151px;top:199px;text-align:center;font-size:7px;color:#fff">Get On Board</div>
</section>

<!-- Home map -->
<section class="phone" style="left:234px;top:56px">
  <span class="time" style="left:18px">9:41</span>
  <svg class="status" style="top:17px"><use href="#status"/></svg>
  <div role="img" aria-label="City street map around the user's location" style="left:6px;top:49px;width:139px;height:268px;border-radius:0 0 16px 16px;background:linear-gradient(180deg,#ffffff 0%,#c9cad6 6%,#3c3f5c 18%,#34374f 100%)"></div>
  <div class="menu" style="left:121px;top:47px"></div>
  <div style="left:13px;top:72px;width:126px;height:21px;border-radius:10px;background:var(--navy);color:var(--amber);font-size:7.5px;font-weight:500;display:flex;align-items:center;justify-content:center">Adds/Message</div>
  <svg class="pin-m" style="left:72px;top:101px"><use href="#pin-light"/></svg>
  <svg class="pin-m" style="left:41px;top:134px"><use href="#pin-light"/></svg>
  <svg class="pin-m" style="left:108px;top:157px"><use href="#pin-light"/></svg>
  <svg class="pin-m" style="left:35px;top:216px"><use href="#pin-light"/></svg>
  <svg class="pin-m" style="left:98px;top:247px"><use href="#pin-light"/></svg>
  <div style="left:45px;top:175px;width:23px;height:23px;border-radius:3px;background:#d9d9dd;border:1px solid #2f3044"></div>
  <div style="left:74px;top:199px;width:11px;height:11px;border-radius:50%;background:#fff;border:2px solid var(--amber)"></div>
  <div style="left:19px;top:276px;width:113px;height:29px;border-radius:5px;background:linear-gradient(90deg,var(--yellow),var(--amber))"></div>
  <div style="left:23px;top:279px;width:105px;height:11px;border-radius:4px;background:var(--navy);color:#fff;font-size:4.3px;display:flex;align-items:center;justify-content:center;padding-left:8px">OPEN YOUR BAG/REWARDS</div>
  <svg style="left:32px;top:277px;width:12px;height:12px" viewBox="0 0 12 12"><rect x="1" y="4" width="10" height="7" rx="1" fill="#fbc30f"/><rect x="0.5" y="3" width="11" height="2.5" fill="#fbed22"/><rect x="5.3" y="3" width="1.4" height="8" fill="#f78f20"/><path d="M6 3C4 0 2 1.5 4 3M6 3c2-3 4-1.5 2 0" stroke="#fbed22" stroke-width="1" fill="none"/></svg>
  <div style="left:23px;top:296px;width:52px;text-align:center;font-size:4px;color:var(--navy)">5000 x jorpoints</div>
  <div style="left:76px;top:294px;width:.5px;height:8px;background:var(--navy)"></div>
  <div style="left:78px;top:296px;width:50px;text-align:center;font-size:4px;color:var(--navy)">5 x voucher</div>
</section>

<!-- Sign up -->
<section class="phone" style="left:220px;top:395px">
  <span class="time" style="left:16px;top:19px">9:41</span>
  <svg class="status" style="top:19px"><use href="#status"/></svg>
  <div style="left:68px;top:30px;width:15px;height:15px;border-radius:50%;background:var(--amber)"></div>
  <div style="left:6px;top:58px;width:139px;height:20px;background:#f6f6f8"></div>
  <div style="left:13px;top:64px;width:58px;text-align:center;font-size:5.5px;color:var(--orange)">Sign Up</div>
  <div style="left:74px;top:61px;width:.5px;height:14px;background:var(--line)"></div>
  <div style="left:78px;top:64px;width:58px;text-align:center;font-size:5.5px;color:var(--muted)">Log In</div>
  <div style="left:13px;top:74px;width:58px;height:2px;background:var(--amber);border-radius:1px"></div>
  <div class="field" style="top:89px">First name</div>
  <div class="field" style="top:113px">Last Name</div>
  <div class="field" style="top:136px">Username</div>
  <div class="field" style="top:160px">Date of Birth</div>
  <div class="field" style="top:184px">Email</div>
  <div class="field" style="top:208px">Referral Code</div>
  <div style="left:20px;top:239px;font-size:5.5px;color:var(--faint)">Gender</div>
  <div style="left:75px;top:231px;width:24px;height:24px;border-radius:4px;box-shadow:0 1px 3px rgba(0,0,0,.12);display:flex;align-items:center;justify-content:center">
    <svg width="12" height="13" viewBox="0 0 12 13"><circle cx="6" cy="4" r="3" fill="none" stroke="#3a3b4a" stroke-width=".8"/><path d="M1 12.5c0-3 2.2-4.8 5-4.8s5 1.8 5 4.8z" fill="none" stroke="#3a3b4a" stroke-width=".8"/></svg>
  </div>
  <div style="left:109px;top:231px;width:24px;height:24px;border-radius:4px;box-shadow:0 1px 3px rgba(0,0,0,.12);display:flex;align-items:center;justify-content:center">
    <svg width="12" height="13" viewBox="0 0 12 13"><circle cx="6" cy="4" r="3" fill="none" stroke="#f78f20" stroke-width=".8"/><path d="M1 12.5c0-3 2.2-4.8 5-4.8s5 1.8 5 4.8z" fill="none" stroke="#f78f20" stroke-width=".8"/></svg>
  </div>
  <div style="left:21px;top:272px;width:116px;height:20px;border-radius:10px;background:linear-gradient(90deg,var(--yellow),var(--orange));color:#fff;font-size:8px;font-weight:600;display:flex;align-items:center;justify-content:center">Sign up</div>
</section>

<!-- Profile -->
<section class="phone" style="left:212px;top:734px">
  <span class="time">9:41</span>
  <svg class="status" style="top:17px"><use href="#status"/></svg>
  <div class="brand" style="left:22px;top:43px"><i></i>jorvix</div>
  <div class="menu" style="left:124px;top:46px"></div>
  <div role="img" aria-label="Member portrait photo" style="left:20px;top:59px;width:47px;height:47px;border-radius:2px;background:linear-gradient(160deg,#8fb0cf,#4a6583)"></div>
  <div style="left:54px;top:91px;width:16px;height:15px;background:var(--amber);color:#fff;font-size:6px;display:flex;align-items:center;justify-content:center">4.5</div>
  <div style="left:77px;top:72px;font-size:7px">Marcel Dufresne</div>
  <div style="left:77px;top:84px;font-size:3.5px;color:var(--muted)">55,000 jorpoints</div>
  <div style="left:21px;top:123px;font-size:6px;font-weight:600;color:var(--title)">Account Details</div>
  <svg style="left:125px;top:122px;width:9px;height:9px" viewBox="0 0 10 10"><rect x=".7" y="1.5" width="7.8" height="7.8" rx="1.5" fill="none" stroke="#f9a51a" stroke-width=".8"/><path d="M4 6.2l.4-1.6L8.3.7l1.2 1.2L5.6 5.8z" fill="none" stroke="#f9a51a" stroke-width=".8"/></svg>
  <div class="label" style="top:145px">Users Name</div>
  <div class="value" style="top:150px">@marcel</div>
  <div class="label" style="top:171px">Phone number</div>
  <div class="value" style="top:176px">+66 555 010</div>
  <div class="label" style="top:197px">Email</div>
  <div class="value" style="top:202px">marcel@mailbox.test</div>
  <div class="nav"></div>
  <div class="nav-pin"><svg><use href="#pin"/></svg></div>
</section>

<!-- Quests -->
<section class="phone" style="left:389px;top:326px">
  <span class="time">9:41</span>
  <svg class="status" style="top:17px"><use href="#status"/></svg>
  <div class="brand" style="left:22px;top:44px"><i></i>jorvix</div>
  <div class="menu" style="left:124px;top:46px"></div>
  <div class="title" style="left:22px;top:69px">Quests Time!</div>
  <div class="sub" style="left:22px;top:81px">Challenge to earn rewards</div>
  <div class="row" style="top:103px"><div class="thumb t-night" role="img" aria-label="Shop photo"></div><div class="rtext"><b>stonelane</b><span>$1 off for any item</span></div><span class="pill">Challenge</span></div>
  <div class="row" style="top:132px"><div class="thumb t-cafe" role="img" aria-label="Cafe menu photo"></div><div class="rtext"><b>mossy cafe</b><span>1 for 1 main dish for dinner</span></div><span class="pill">Challenge</span></div>
  <div class="row" style="top:162px"><div class="thumb t-salon" role="img" aria-label="Salon flyer photo"></div><div class="rtext"><b>nextroom</b><span>$10 off for all hair services</span></div><span class="pill">Challenge</span></div>
  <div class="row" style="top:191px"><div class="thumb t-night" role="img" aria-label="Shop photo"></div><div class="rtext"><b>stonelane</b><span>$1 off for any item</span></div><span class="pill">Challenge</span></div>
  <div class="row" style="top:220px"><div class="thumb t-cafe" role="img" aria-label="Cafe menu photo"></div><div class="rtext"><b>mossy cafe</b><span>1 for 1 main dish for dinner</span></div><span class="pill">Challenge</span></div>
  <div class="row" style="top:250px;border:0"><div class="thumb t-salon" role="img" aria-label="Salon flyer photo"></div><div class="rtext"><b>nextroom</b><span>$10 off for all hair services</span></div><span class="pill">Challenge</span></div>
  <div class="nav"></div>
  <div class="nav-pin"><svg><use href="#pin"/></svg></div>
</section>

<!-- Wallet -->
<section class="phone" style="left:387px;top:663px">
  <span class="time">9:41</span>
  <svg class="status" style="top:17px"><use href="#status"/></svg>
  <div class="brand" style="left:22px;top:43px"><i></i>jorvix</div>
  <div class="menu" style="left:124px;top:46px"></div>
  <div role="img" aria-label="Member portrait photo" style="left:22px;top:65px;width:24px;height:23px;border-radius:2px;background:linear-gradient(160deg,#8fb0cf,#4a6583)"></div>
  <div style="left:39px;top:82px;width:7px;height:6px;background:var(--amber);color:#fff;font-size:2.5px;display:flex;align-items:center;justify-content:center">4.5</div>
  <div style="left:48px;top:71px;font-size:4.5px;color:var(--title)">Marcel Dufresne</div>
  <div style="left:48px;top:78px;font-size:3px;color:var(--muted)">55,000 jorpoints</div>
  <span class="pill" style="left:115px;top:73px;width:20px;height:5px;font-size:1.8px">View Account</span>
  <div style="left:6px;top:96px;width:139px;height:16px;background:#f8f8fa"></div>
  <div style="left:14px;top:98px;width:57px;text-align:center;font-size:5.5px;color:var(--orange)">vouchers</div>
  <div style="left:73px;top:98px;width:.5px;height:12px;background:var(--line)"></div>
  <div style="left:80px;top:100px;width:66px;text-align:center;font-size:5.5px;color:var(--muted)">Swarm</div>
  <div style="left:14px;top:108px;width:57px;height:2px;background:var(--amber)"></div>
  <div class="row" style="top:122px;left:6px"><div class="thumb t-night" style="left:10px" role="img" aria-label="Shop photo"></div><div class="rtext" style="left:34px"><b>stonelane</b><span>$1 off for any item</span></div><span class="pill" style="left:98px;width:28px;font-size:4.5px">Claim</span></div>
  <div class="row" style="top:151px"><div class="thumb t-cafe" style="left:10px" role="img" aria-label="Cafe menu photo"></div><div class="rtext" style="left:34px"><b>mossy cafe</b><span>1 for 1 main dish for dinner</span></div><span class="pill" style="left:98px;width:28px;font-size:4.5px">Claim</span></div>
  <div class="row" style="top:181px"><div class="thumb t-salon" style="left:10px" role="img" aria-label="Salon flyer photo"></div><div class="rtext" style="left:34px"><b>nextroom</b><span>$10 off for all hair services</span></div><span class="pill" style="left:98px;width:28px;font-size:4.5px">Claim</span></div>
  <div class="row" style="top:212px"><div class="thumb t-night" style="left:10px" role="img" aria-label="Shop photo"></div><div class="rtext" style="left:34px"><b>stonelane</b><span>$1 off for any item</span></div><span class="pill" style="left:98px;width:28px;font-size:4.5px">Claim</span></div>
  <div class="row" style="top:240px"><div class="thumb t-cafe" style="left:10px" role="img" aria-label="Cafe menu photo"></div><div class="rtext" style="left:34px"><b>mossy cafe</b><span>1 for 1 main dish for dinner</span></div><span class="pill" style="left:98px;width:28px;font-size:4.5px">Claim</span></div>
  <div style="left:20px;top:273px;width:8px;height:8px;border-radius:50%;background:var(--amber)"></div>
  <div style="left:30px;top:273px;font-size:4.5px;font-weight:600;color:var(--title)">Tips</div>
  <div style="left:53px;top:272px;width:70px;font-size:3.3px;line-height:1.2;color:var(--ink)">travel and challenge our quests to earn more point</div>
  <div class="nav"></div>
  <div class="nav-pin"><svg><use href="#pin"/></svg></div>
</section>

<!-- Exchange -->
<section class="phone" style="left:555px;top:145px">
  <span class="time" style="left:18px">9:41</span>
  <svg class="status" style="top:17px"><use href="#status"/></svg>
  <div class="brand" style="left:22px;top:44px"><i></i>jorvix</div>
  <div class="menu" style="left:121px;top:46px"></div>
  <div class="title" style="left:23px;top:69px">Exchange Time!</div>
  <div class="sub" style="left:23px;top:81px">55,000 jorpoints</div>
  <div class="row" style="top:100px"><span style="left:17px;top:11px;width:22px;height:2px;background:#3a3b4a"></span><div class="rtext" style="left:45px"><b>Stonelane</b><span>$0.50 off any food item</span><span>4000 JorCoins</span></div><span class="pill" style="left:104px;top:7px">Claim It</span><span style="left:9px;top:22px;width:40px;height:1.5px;background:linear-gradient(90deg,var(--yellow),var(--orange))"></span></div>
  <div class="row" style="top:128px"><span style="left:17px;top:11px;width:22px;height:2px;background:#3a3b4a"></span><div class="rtext" style="left:45px"><b>Stonelane</b><span>$0.50 off any food item</span><span>4000 JorCoins</span></div><span class="pill" style="left:104px;top:7px">Claim It</span><span style="left:9px;top:22px;width:40px;height:1.5px;background:linear-gradient(90deg,var(--yellow),var(--orange))"></span></div>
  <div class="row" style="top:159px"><span style="left:17px;top:11px;width:22px;height:2px;background:#3a3b4a"></span><div class="rtext" style="left:45px"><b>Stonelane</b><span>$0.50 off any food item</span><span>4000 JorCoins</span></div><span class="pill" style="left:104px;top:8px">Claim It</span><span style="left:9px;top:22px;width:40px;height:1.5px;background:linear-gradient(90deg,var(--yellow),var(--orange))"></span></div>
  <div class="row" style="top:188px"><span style="left:17px;top:9px;width:22px;height:2px;background:#3a3b4a"></span><div class="rtext" style="left:45px;top:2px"><b>Stonelane</b><span>$0.50 off any food item</span><span>4000 JorCoins</span></div><span class="pill" style="left:104px;top:6px">Claim It</span><span style="left:9px;top:20px;width:40px;height:1.5px;background:linear-gradient(90deg,var(--yellow),var(--orange))"></span></div>
  <div class="row" style="top:217px"><span style="left:17px;top:10px;width:22px;height:2px;background:#3a3b4a"></span><div class="rtext" style="left:45px;top:3px"><b>Stonelane</b><span>$0.50 off any food item</span><span>4000 JorCoins</span></div><span class="pill" style="left:104px;top:6px">Claim It</span><span style="left:9px;top:21px;width:40px;height:1.5px;background:linear-gradient(90deg,var(--yellow),var(--orange))"></span></div>
  <div class="row" style="top:247px;border:0"><span style="left:17px;top:10px;width:22px;height:2px;background:#3a3b4a"></span><div class="rtext" style="left:45px;top:3px"><b>Stonelane</b><span>$0.50 off any food item</span><span>4000 JorCoins</span></div><span class="pill" style="left:104px;top:7px">Claim It</span><span style="left:9px;top:22px;width:40px;height:1.5px;background:linear-gradient(90deg,var(--yellow),var(--orange))"></span></div>
  <div class="nav"></div>
  <div class="nav-pin"><svg><use href="#pin"/></svg></div>
</section>

<!-- Partners -->
<section class="phone" style="left:552px;top:484px">
  <span class="time">9:41</span>
  <svg class="status" style="top:17px"><use href="#status"/></svg>
  <div class="brand" style="left:22px;top:44px"><i></i>jorvix</div>
  <div class="menu" style="left:121px;top:46px"></div>
  <div class="title" style="left:22px;top:69px">Partners</div>
  <div class="sub" style="left:22px;top:81px">Our esteem contributors</div>
  <div class="row" style="top:94px"><div class="thumb t-night" role="img" aria-label="Shop photo"></div><div class="rtext"><b>stonelane</b><span>$1 off for any item</span></div><span class="pill" style="left:105px;width:28px">Read Profile</span></div>
  <div class="row" style="top:124px"><div class="thumb t-cafe" role="img" aria-label="Cafe menu photo"></div><div class="rtext"><b>mossy cafe</b><span>1 for 1 main dish for dinner</span></div><span class="pill" style="left:105px;width:28px">Read Profile</span></div>
  <div class="row" style="top:154px"><div class="thumb t-salon" role="img" aria-label="Salon flyer photo"></div><div class="rtext"><b>nextroom</b><span>$10 off for all hair services</span></div><span class="pill" style="left:105px;width:28px">Read Profile</span></div>
  <div class="row" style="top:184px"><div class="thumb t-night" role="img" aria-label="Shop photo"></div><div class="rtext"><b>stonelane</b><span>$1 off for any item</span></div><span class="pill" style="left:105px;width:28px">Read Profile</span></div>
  <div class="row" style="top:213px"><div class="thumb t-cafe" role="img" aria-label="Cafe menu photo"></div><div class="rtext"><b>mossy cafe</b><span>1 for 1 main dish for dinner</span></div><span class="pill" style="left:105px;width:28px">Read Profile</span></div>
  <div class="row" style="top:243px;border:0"><div class="thumb t-salon" role="img" aria-label="Salon flyer photo"></div><div class="rtext"><b>nextroom</b><span>$10 off for all hair services</span></div><span class="pill" style="left:105px;width:28px">Read Profile</span></div>
  <div class="nav"></div>
  <div class="nav-pin"><svg><use href="#pin"/></svg></div>
</section>

<!-- Side menu -->
<section class="phone" style="left:553px;top:819px">
  <div role="img" aria-label="Blurred view of the home screen behind the menu" style="left:6px;top:11px;width:139px;height:307px;border-radius:16px;background:linear-gradient(180deg,#b9bac3 0%,#9a9cab 45%,#7d7f92 100%)"></div>
  <div style="left:88px;top:11px;width:57px;height:307px;background:var(--navy);border-radius:0 16px 16px 0"></div>
  <div class="notch" style="top:11px"></div>
  <span class="time" style="left:18px;top:19px;color:#fff">9:41</span>
  <svg class="status" style="top:19px;color:#fff"><use href="#status"/></svg>
  <div class="menu" style="left:102px;top:41px;border-color:#fff"></div>
  <style>.phone .menu[style*="border-color:#fff"]::after{background:#fff}</style>
  <div class="menu-item" style="top:73px">Home</div>
  <div class="menu-item" style="top:85px">My Account</div>
  <div class="menu-item" style="top:100px">Partners</div>
  <div class="menu-item" style="top:114px">Guide</div>
  <div class="menu-item" style="top:128px">Terms of Use</div>
  <div class="menu-item" style="top:143px">Privacy Policy</div>
  <div class="menu-item" style="top:158px">Chat with us</div>
  <div style="left:103px;top:192px;width:24px;height:24px;border-radius:50%;background:var(--amber)"></div>
  <div class="menu-item" style="top:268px">Settings</div>
  <div class="menu-item" style="top:284px">Sign Out</div>
</section>

<div style="position:absolute;left:408px;top:174px;width:6px;height:6px;border-radius:50%;background:#7cc242"></div>

</body>
</html>
```